Brochure for medical doctor

I need a brochure for a medical doctor to promote his practice. The brochure should contain his picture, business information (use letterhead from attachment), and the following text:

- Now accepting PI cases on lien!
- Same and next business day appointments available for initial visits, pre-operative clearances, and all other medical needs

- Expedited medical reports sent quickly to your office

Industry/Entity Type

Medical

```html
<!DOCTYPE html>
<html lang="en">
<head>
<meta charset="utf-8">
<title>Holloway Medical Center – Brochure</title>
<link rel="stylesheet" href="https://fonts.googleapis.com/css2?family=Tinos:wght@700&family=Poppins:wght@500;600&family=Arimo:wght@400&display=swap">
<style>
  :root {
    --brand-blue: #163d8f;
    --brand-green: #52e046;
    --paper: #f7f7f7;
    --white: #ffffff;
  }
  html, body {
    margin: 0;
    padding: 0;
    width: 848px;
    height: 1200px;
    overflow: hidden;
    background: var(--paper);
  }
  .brochure {
    position: relative;
    width: 848px;
    height: 1200px;
    overflow: hidden;
    background: var(--paper);
  }
  .decor, .portrait-frame, .icon {
    position: absolute;
    display: block;
  }
  .brand {
    position: absolute;
    left: 28px;
    top: 143px;
    width: 796px;
    display: flex;
    align-items: center;
    gap: 20px;
  }
  .brand-mark {
    flex: none;
    width: 58px;
    height: 58px;
    background: var(--brand-blue);
  }
  .brand-name {
    margin: 0;
    font-family: "Tinos", "Times New Roman", serif;
    font-weight: 700;
    font-size: 43px;
    line-height: 1;
    letter-spacing: -0.3px;
    color: var(--brand-blue);
    white-space: nowrap;
  }
  .offer-outline {
    position: absolute;
    left: 72px;
    top: 884px;
    width: 525px;
    height: 178px;
    border: 2px solid var(--brand-green);
    border-radius: 28px;
  }
  .offer-panel {
    position: absolute;
    left: 57px;
    top: 866px;
    width: 531px;
    height: 184px;
    background: var(--brand-blue);
    border-radius: 26px;
  }
  .offer-tab {
    position: absolute;
    left: 82px;
    top: 823px;
    width: 486px;
    height: 64px;
    background: var(--brand-green);
    border-radius: 13px;
    box-sizing: border-box;
    padding-left: 25px;
    display: flex;
    align-items: center;
  }
  .offer-headline {
    margin: 0;
    font-family: "Poppins", Arial, sans-serif;
    font-weight: 600;
    font-size: 28px;
    color: var(--white);
    white-space: nowrap;
    letter-spacing: -0.3px;
  }
  .offer-body {
    position: absolute;
    left: 93px;
    top: 912px;
    width: 480px;
    font-family: "Arimo", Arial, sans-serif;
    font-size: 20.5px;
    line-height: 24px;
    color: var(--white);
  }
  .offer-body p { margin: 0; }
  .offer-body p + p { margin-top: 22px; }
  .contact {
    position: absolute;
    top: 1106px;
    left: 0;
    width: 848px;
    height: 28px;
    font-family: "Poppins", Arial, sans-serif;
    font-weight: 500;
    font-size: 15.5px;
    color: var(--brand-blue);
  }
  .contact-item {
    position: absolute;
    top: 0;
    height: 28px;
    display: flex;
    align-items: center;
    white-space: nowrap;
  }
  .contact-item .icon { position: static; margin-right: 8px; }
  .contact-address { left: 82px; }
  .contact-phone { left: 452px; }
  .contact-fax { left: 628px; }
</style>
</head>
<body>
<main class="brochure">

  <svg class="decor dot-grid-top" style="left:12px;top:7px" width="154" height="96" viewBox="0 0 154 96" aria-hidden="true">
    <defs><pattern id="blueDots" width="21" height="18" patternUnits="userSpaceOnUse"><circle cx="2" cy="2" r="1.7" fill="#163d8f"/></pattern></defs>
    <rect width="154" height="96" fill="url(#blueDots)"/>
  </svg>

  <svg class="decor plus-small-blue" style="left:598px;top:16px" width="35" height="35" viewBox="0 0 100 100" aria-hidden="true">
    <rect x="38" y="0" width="24" height="100" rx="12" fill="#163d8f"/>
    <rect x="0" y="38" width="100" height="24" rx="12" fill="#163d8f"/>
  </svg>

  <header class="brand">
    <span class="brand-mark"></span>
    <h1 class="brand-name">HOLLOWAY MEDICAL CENTER</h1>
  </header>

  <svg class="decor plus-outline-blue" style="left:103px;top:308px" width="82" height="82" viewBox="-6 -6 112 112" aria-hidden="true">
    <path d="M30,30 V20 A20,20 0 0 1 70,20 V30 H80 A20,20 0 0 1 80,70 H70 V80 A20,20 0 0 1 30,80 V70 H20 A20,20 0 0 1 20,30 Z" fill="none" stroke="#163d8f" stroke-width="10" stroke-linejoin="round"/>
  </svg>

  <svg class="decor plus-green" style="left:746px;top:270px" width="43" height="43" viewBox="0 0 100 100" aria-hidden="true">
    <rect x="36" y="0" width="28" height="100" rx="14" fill="#52e046"/>
    <rect x="0" y="36" width="100" height="28" rx="14" fill="#52e046"/>
  </svg>

  <svg class="decor plus-green" style="left:280px;top:575px" width="43" height="43" viewBox="0 0 100 100" aria-hidden="true">
    <rect x="36" y="0" width="28" height="100" rx="14" fill="#52e046"/>
    <rect x="0" y="36" width="100" height="28" rx="14" fill="#52e046"/>
  </svg>

  <svg class="portrait-frame" style="left:0;top:0" width="848" height="800" viewBox="0 0 848 800">
    <path d="M478,391 L790,397 Q850,400 880,460 L880,734 L460,734 L430,470 Q425,391 478,391 Z" fill="none" stroke="#52e046" stroke-width="2.5"/>
    <path role="img" aria-label="Portrait of the smiling doctor in a white coat with a stethoscope, arms crossed"
          d="M430,432 L730,437 Q785,440 785,500 L785,722 Q785,770 745,770 L470,770 Q420,760 410,700 L380,495 Q375,432 430,432 Z" fill="#163d8f"/>
    <defs><pattern id="greenDots" width="25.5" height="21.8" patternUnits="userSpaceOnUse"><circle cx="2" cy="2" r="2" fill="#52e046"/></pattern></defs>
    <rect x="737" y="600" width="111" height="115" fill="url(#greenDots)"/>
  </svg>

  <svg class="decor plus-outline-green" style="left:687px;top:914px" width="60" height="60" viewBox="-6 -6 112 112" aria-hidden="true">
    <path d="M30,30 V20 A20,20 0 0 1 70,20 V30 H80 A20,20 0 0 1 80,70 H70 V80 A20,20 0 0 1 30,80 V70 H20 A20,20 0 0 1 20,30 Z" fill="none" stroke="#52e046" stroke-width="10" stroke-linejoin="round"/>
  </svg>

  <section class="offer">
    <div class="offer-outline"></div>
    <div class="offer-panel"></div>
    <div class="offer-tab"><h2 class="offer-headline">Now accepting PI cases on lien!</h2></div>
    <div class="offer-body">
      <p>Same and next business day appointments available for initial visits, pre-operative clearances, and all other medical needs</p>
      <p>Expedited medical reports sent quickly to your office</p>
    </div>
  </section>

  <footer class="contact">
    <div class="contact-item contact-address">
      <svg class="icon" width="18" height="27" viewBox="0 0 24 36" aria-hidden="true">
        <path d="M12,0 C5.4,0 0,5.2 0,11.8 C0,20 12,36 12,36 C12,36 24,20 24,11.8 C24,5.2 18.6,0 12,0 Z M12,16.5 A5,5 0 1 1 12,6.5 A5,5 0 1 1 12,16.5 Z" fill="#163d8f"/>
      </svg>
      <span>4120 Linden Ave. Lakeview, CA, 90000</span>
    </div>
    <div class="contact-item contact-phone">
      <svg class="icon" width="26" height="26" viewBox="0 0 24 24" aria-hidden="true">
        <path d="M6.6,10.8 C8,13.6 10.4,16 13.2,17.4 L15.4,15.2 C15.7,14.9 16.1,14.8 16.4,15 C17.5,15.4 18.7,15.6 20,15.6 C20.6,15.6 21,16 21,16.6 V20 C21,20.6 20.6,21 20,21 C10.6,21 3,13.4 3,4 C3,3.4 3.4,3 4,3 H7.5 C8.1,3 8.5,3.4 8.5,4 C8.5,5.3 8.7,6.5 9.1,7.6 C9.2,7.9 9.1,8.3 8.9,8.6 Z" fill="#163d8f"/>
      </svg>
      <span>(555) 014-2200</span>
    </div>
    <div class="contact-item contact-fax">
      <svg class="icon" width="29" height="28" viewBox="0 0 28 27" aria-hidden="true">
        <rect x="7" y="0" width="14" height="6" fill="#163d8f"/>
        <rect x="0" y="7" width="28" height="12" rx="2" fill="#163d8f"/>
        <rect x="7" y="16" width="14" height="11" fill="#163d8f" stroke="#f7f7f7" stroke-width="1.5"/>
        <rect x="22" y="10" width="3" height="2" fill="#f7f7f7"/>
      </svg>
      <span>(555) 014-2207</span>
    </div>
  </footer>

</main>
</body>
</html>
```